Plakat für Hausverwaltung
Zielgruppe
Hausverwaltung
(Verwaltung von Wohn- und Gewerbeimmobilien)
Aufgabenstellung
Es soll ein Werbeplakat werden, Die Inhalte der Dienstleistung und die Firmenfarben kann der Webseite entnommen werden.
Ein guter Werbespruch und ansprechendes Desing ohne viel Schrift.

```html
<!DOCTYPE html>
<html lang="de">
<head>
<meta charset="utf-8">
<title>Lindwerk Hausverwaltung – Plakat</title>
<link href="https://fonts.googleapis.com/css2?family=Montserrat:wght@300;400;900&display=swap" rel="stylesheet">
<style>
  :root {
    --sand: #cdc5c0;
    --sand-light: #d6cfca;
    --ink: #000000;
    --paper: #ffffff;
    --text-dark: #1a1a1a;
  }
  * { margin: 0; padding: 0; box-sizing: border-box; }
  html, body { width: 920px; height: 1200px; overflow: hidden; background: var(--paper); }
  .poster {
    position: relative; width: 920px; height: 1200px;
    background: var(--ink); font-family: "Montserrat", sans-serif; overflow: hidden;
  }
  .top-band {
    position: absolute; left: 0; top: 0; width: 920px; height: 89px; background: var(--sand);
  }
  .brand {
    position: absolute; left: 42px; top: 34px;
    font-size: 19px; font-weight: 400; color: var(--text-dark); white-space: nowrap;
  }
  .skyline-area {
    position: absolute; left: 368px; top: 12px; width: 552px; height: 64px;
    background: linear-gradient(90deg, var(--sand), var(--sand-light));
  }
  .headline {
    position: absolute; left: 56px; top: 168px; width: 860px;
    color: var(--paper); font-weight: 900; font-size: 95px; line-height: 112px;
    letter-spacing: -1.5px; transform: rotate(-4deg); transform-origin: left top;
    white-space: nowrap;
  }
  .claim {
    position: absolute; left: 58px; top: 640px; width: 815px;
    transform: rotate(-4.3deg); transform-origin: left top;
    color: var(--paper); font-weight: 400; font-size: 45px; letter-spacing: 0.5px;
  }
  .claim-line {
    display: block; height: 62px; line-height: 62px; padding-top: 4px;
    border-bottom: 1px solid var(--paper); white-space: nowrap;
  }
  .claim-line:first-child { border-top: 1px solid var(--paper); }
  .services { position: absolute; left: 62px; top: 918px; list-style: none; color: var(--paper); }
  .services li {
    display: flex; align-items: center; height: 35px; font-size: 16px; font-weight: 300; letter-spacing: 0.5px;
  }
  .services svg { width: 16px; height: 16px; margin-right: 28px; }
  .team-photo {
    position: absolute; left: 360px; top: 871px; width: 560px; height: 223px;
    background: linear-gradient(180deg, #e8e6e2 0%, #c9c5c0 40%, #6b6f78 100%);
  }
  .bottom-band {
    position: absolute; left: 0; top: 1094px; width: 920px; height: 106px; background: var(--sand);
    color: var(--text-dark);
  }
  .contact-title { position: absolute; left: 206px; top: 22px; font-size: 23px; font-weight: 400; }
  .contact-item { position: absolute; top: 14px; font-size: 9px; line-height: 11px; }
  .contact-item svg { display: block; margin-bottom: 8px; }
  .contact-address { left: 358px; }
  .contact-mail { left: 515px; }
  .contact-phone { left: 668px; }
</style>
</head>
<body>
<div class="poster">
  <header class="top-band">
    <div class="brand">Lindwerk Hausverwaltung GmbH</div>
    <div class="skyline-area" role="img" aria-label="Linienzeichnung einer Häuserreihe"></div>
  </header>

  <h1 class="headline">Suchen Sie<br>einen Verwalter<br>für Ihre<br>Immobilie?</h1>

  <p class="claim">
    <span class="claim-line">Wir bieten Ihnen profesionelle,</span>
    <span class="claim-line">reibungslose und zuverlässige</span>
    <span class="claim-line">Verwaltung.</span>
  </p>

  <ul class="services">
    <li><svg viewBox="0 0 16 16"><path d="M1 7 L8 1 L15 7 V15 H1 Z" fill="#fff"/></svg>Wohnungsverwaltung</li>
    <li><svg viewBox="0 0 16 16"><path d="M1 7 L8 1 L15 7 V15 H1 Z" fill="#fff"/></svg>Sondereigentum</li>
    <li><svg viewBox="0 0 16 16"><path d="M1 7 L8 1 L15 7 V15 H1 Z" fill="#fff"/></svg>Mietverwaltung</li>
  </ul>

  <div class="team-photo" role="img" aria-label="Foto des dreiköpfigen Verwaltungsteams vor einem Regal mit Aktenordnern"></div>

  <footer class="bottom-band">
    <div class="contact-title">Kontakt</div>
    <div class="contact-item contact-address">
      <svg width="24" height="24" viewBox="0 0 24 24"><path d="M2 11 L12 2 L22 11 V22 H2 Z" fill="none" stroke="#1a1a1a" stroke-width="1.3"/></svg>
      Lindenweg 12<br>35039 Talstadt
    </div>
    <div class="contact-item contact-mail">
      <svg width="26" height="24" viewBox="0 0 26 24"><rect x="1" y="7" width="24" height="13" fill="none" stroke="#1a1a1a" stroke-width="1.3"/><path d="M1 7 L13 15 L25 7" fill="none" stroke="#1a1a1a" stroke-width="1.3"/></svg>
      info@lindwerk-verwaltung.de
    </div>
    <div class="contact-item contact-phone">
      <svg width="18" height="26" viewBox="0 0 18 26"><rect x="2" y="1" width="14" height="24" rx="2" fill="none" stroke="#1a1a1a" stroke-width="1.3"/><line x1="2" y1="20" x2="16" y2="20" stroke="#1a1a1a" stroke-width="1.3"/></svg>
      01234 567890
    </div>
  </footer>
</div>
</body>
</html>
```